Velmorra Aviation - Insurance Brokers - Half page magazine ad.

Half-page ad in an aviation industry magazine promoting our services as an aviation insurance broker. I've attached an example of a pop-up banner we used at a conference recently to give you an idea.

I have attached a copy of the specifications from the publisher. Half-page ad requires:
- 190mm width x 132mm height
- Minimum 300 dpi
- colours in CMYK
- high resolution PDF with fonts embedded

Target Market(s)

Aircraft owners/operators, drone owners/operators, pilots

Font styles to use
Serif

Colors

Designer to choose colors to be used in the design.

Requirements
Must have
• 1. Company logo (attached).
• 2. Contact Details as follows:
• www.qtnaviation.com.au
• (02) 4193 7625
Nice to have
• Maybe a picture of an aircraft/helicopter in the bakground with logo/text etc over the top. But happy to look at alternative design options.

```html
<!DOCTYPE html>
<html lang="en">
<head>
<meta charset="utf-8">
<title>Velmorra Aviation – Half Page Ad</title>
<link rel="stylesheet" href="https://fonts.googleapis.com/css2?family=Montserrat:wght@500;600;700;800&display=swap">
<style>
  :root {
    --navy: #1c2a6b;
    --red: #c8102e;
    --sky-top: #d3e2f2;
    --sky-mid: #a9c7e6;
    --sea: #3ea2c6;
    --sea-deep: #1f7fa8;
    --white: #ffffff;
  }
  * { margin: 0; padding: 0; box-sizing: border-box; }
  html, body { width: 1200px; height: 862px; overflow: hidden; background: #e9ecef; }
  .ad {
    position: relative;
    width: 1200px; height: 862px;
    overflow: hidden;
    font-family: "Montserrat", sans-serif;
    color: var(--navy);
  }
  .scene-photo {
    position: absolute; inset: 0;
    background: linear-gradient(180deg, var(--sky-top) 0%, var(--sky-mid) 72%, var(--sea) 80%, var(--sea-deep) 100%);
  }
  .aircraft-photo {
    position: absolute; left: 560px; top: 450px; width: 560px; height: 300px;
    border-radius: 50%;
    background: radial-gradient(ellipse at center, rgba(120,135,150,0.55) 0%, rgba(120,135,150,0) 70%);
  }
  .brand {
    position: absolute; left: 60px; top: 48px;
    display: flex; align-items: center; gap: 16px;
  }
  .brand-mark { width: 44px; height: 44px; background: var(--navy); }
  .brand-name { font-size: 40px; font-weight: 700; color: var(--navy); letter-spacing: 0.5px; }
  .phone {
    position: absolute; right: 70px; top: 175px;
    display: flex; align-items: center; gap: 14px;
    color: var(--red); font-weight: 700; font-size: 32px; letter-spacing: 1px;
  }
  .headline {
    position: absolute; left: 60px; top: 240px;
    font-weight: 800; font-size: 64px; line-height: 1.1; letter-spacing: 1.5px;
  }
  .headline .accent { color: var(--red); display: block; }
  .headline .main { color: var(--navy); display: block; }
  .services {
    position: absolute; left: 66px; top: 420px; list-style: none;
  }
  .services li {
    display: flex; align-items: center; gap: 14px;
    font-size: 25px; font-weight: 600; text-transform: uppercase;
    color: var(--navy); height: 42px; letter-spacing: 0.5px;
  }
  .services li::before {
    content: ""; width: 12px; height: 12px; border-radius: 50%; background: var(--red);
  }
  .web {
    position: absolute; left: 60px; bottom: 62px;
    display: flex; align-items: center; gap: 12px;
    font-size: 30px; font-weight: 600; color: var(--navy);
  }
</style>
</head>
<body>
  <main class="ad">
    <div class="scene-photo" role="img" aria-label="Photograph of a grey navy helicopter flying over a blue sea with a green island on the horizon"></div>
    <div class="aircraft-photo" role="img" aria-label="Helicopter in flight"></div>

    <header class="brand">
      <span class="brand-mark"></span>
      <span class="brand-name">Velmorra Aviation</span>
    </header>

    <div class="phone">
      <svg width="34" height="34" viewBox="0 0 34 34" aria-hidden="true">
        <circle cx="17" cy="17" r="15" fill="none" stroke="#1c2a6b" stroke-width="2.5"/>
        <path d="M12 10c1-1 2-1 2.6 0l1.6 2.6c.4.7.2 1.4-.4 1.9l-1 .8c.8 1.8 2.1 3.1 3.9 3.9l.8-1c.5-.6 1.2-.8 1.9-.4L24 19.4c1 .6 1 1.6 0 2.6-1.4 1.4-3 1.7-5 .8-3.2-1.4-5.4-3.6-6.8-6.8-.9-2-.6-3.6.8-5z" fill="#1c2a6b"/>
      </svg>
      <span>(02) 4193 7625</span>
    </div>

    <h1 class="headline">
      <span class="accent">SPECIALIST AVIATION</span>
      <span class="main">INSURANCE BROKERS</span>
    </h1>

    <ul class="services">
      <li>Fixedwing</li>
      <li>Rotorwing</li>
      <li>MROs</li>
      <li>Manufacturers</li>
      <li>Drones</li>
      <li>Loss of Licence</li>
      <li>Personal Accident</li>
    </ul>

    <div class="web">
      <svg width="30" height="30" viewBox="0 0 30 30" aria-hidden="true">
        <circle cx="15" cy="15" r="13" fill="#c8102e"/>
        <g fill="none" stroke="#fff" stroke-width="1.6">
          <ellipse cx="15" cy="15" rx="5.5" ry="13"/>
          <line x1="2" y1="15" x2="28" y2="15"/>
          <path d="M4.5 8.5h21M4.5 21.5h21"/>
        </g>
      </svg>
      <span>www.qtnaviation.com.au</span>
    </div>
  </main>
</body>
</html>
```